Diagram of Marrowfen’s history for website

This project is to design the attached diagram along the lines of the attached image but in our branding - style guide attached. The diagram will be going on the Marrowfen website - www.marrowfen.au.

```html
<!DOCTYPE html>
<html lang="en">
<head>
<meta charset="utf-8">
<title>Marrowfen History</title>
<link href="https://fonts.googleapis.com/css2?family=Montserrat:wght@400;500;700&display=swap" rel="stylesheet">
<style>
  :root{
    --sage:#6f9a80;
    --slate:#7fa1a8;
    --peach:#d8a791;
    --ink:#222222;
    --bar:#e6e6e6;
    --frame:#b9cbc3;
    --paper:#ffffff;
    --backdrop:#f2f2f2;
    --scheme:#5b2f78;
  }
  *{margin:0;padding:0;box-sizing:border-box}
  html,body{width:1200px;height:1200px;overflow:hidden;background:var(--backdrop);font-family:"Montserrat",Arial,sans-serif;color:var(--ink)}
  .sheet{position:absolute;left:20px;top:152px;width:1160px;height:896px;background:var(--paper)}
  .frame{position:absolute;left:19px;top:19px;right:18px;bottom:19px;border:1.5px solid var(--frame)}
  .brand{position:absolute;display:flex;align-items:center;gap:8px;font-weight:700;color:var(--sage);white-space:nowrap}
  .brand-main{left:78px;top:116px;font-size:21px}
  .brand-dot{width:24px;height:24px;border-radius:50%;background:var(--sage);flex:none}
  .title{position:absolute;left:266px;top:72px;font-size:44px;font-weight:500;letter-spacing:-.3px;line-height:1.1;white-space:nowrap}
  .title-rule{position:absolute;left:244px;top:126px;width:424px;height:1.5px;background:var(--slate)}
  .timeline{position:absolute;left:109px;top:470px;width:840px;height:22px}
  .timeline-band{position:absolute;left:10px;top:0;width:822px;height:22px;background:var(--bar)}
  .year{position:absolute;top:-4px;display:flex;align-items:center;gap:8px;font-weight:700;font-size:17px}
  .year svg{width:24px;height:30px}
  .stem{position:absolute;width:0;border-left:2.5px dotted}
  .event{position:absolute;width:170px}
  .event h3{font-size:13.5px;font-weight:700;text-transform:uppercase;line-height:1.15;margin-bottom:4px;padding-bottom:2px;border-bottom:1px solid currentColor;display:inline-block}
  .event p{font-size:11.5px;line-height:1.25;color:var(--ink)}
  .icon{position:absolute;width:34px;height:34px}
  .icon svg{width:100%;height:100%;fill:none;stroke-width:1.8;stroke-linecap:round;stroke-linejoin:round}
  .c-sage{color:var(--sage)} .c-slate{color:var(--slate)} .c-peach{color:var(--peach)}
  .badge-square{position:absolute;width:44px;height:38px;background:var(--scheme);border-radius:2px}
  .badge-circle{position:absolute;width:30px;height:30px;border-radius:50%}
  .wordmark{position:absolute;font-weight:700;white-space:nowrap}
</style>
</head>
<body>
<div class="sheet">
  <div class="frame"></div>

  <div class="brand brand-main"><span class="brand-dot"></span>Marrowfen</div>
  <h1 class="title">Marrowfen History</h1>
  <div class="title-rule"></div>

  <div class="timeline">
    <div class="timeline-band"></div>
    <div class="year" style="left:0"><svg viewBox="0 0 24 30"><path d="M0 0H12L24 15L12 30H0L12 15Z" fill="var(--sage)"/></svg>2017</div>
    <div class="year" style="left:160px"><svg viewBox="0 0 24 30"><path d="M0 0H12L24 15L12 30H0L12 15Z" fill="var(--slate)"/></svg>2018</div>
    <div class="year" style="left:319px"><svg viewBox="0 0 24 30"><path d="M0 0H12L24 15L12 30H0L12 15Z" fill="var(--peach)"/></svg>2019</div>
    <div class="year" style="left:478px"><svg viewBox="0 0 24 30"><path d="M0 0H12L24 15L12 30H0L12 15Z" fill="var(--sage)"/></svg>2021</div>
    <div class="year" style="left:637px"><svg viewBox="0 0 24 30"><path d="M0 0H12L24 15L12 30H0L12 15Z" fill="var(--slate)"/></svg>2022</div>
    <div class="year" style="left:796px"><svg viewBox="0 0 24 30"><path d="M0 0H12L24 15L12 30H0L12 15Z" fill="var(--peach)"/></svg>2023</div>
  </div>

  <div class="stem" style="left:278px;top:362px;height:87px;border-color:var(--sage)"></div>
  <div class="stem" style="left:667px;top:366px;height:83px;border-color:var(--sage)"></div>
  <div class="stem" style="left:914px;top:378px;height:71px;border-color:var(--peach)"></div>
  <div class="stem" style="left:119px;top:508px;height:90px;border-color:var(--sage)"></div>
  <div class="stem" style="left:439px;top:508px;height:90px;border-color:var(--peach)"></div>
  <div class="stem" style="left:755px;top:508px;height:90px;border-color:var(--slate)"></div>

  <div class="icon c-sage" style="left:228px;top:266px"><svg viewBox="0 0 34 34" stroke="currentColor"><path d="M17 26s8-8 8-14a8 8 0 0 0-16 0c0 6 8 14 8 14z"/><circle cx="17" cy="12" r="3"/><path d="M6 30h22"/></svg></div>
  <div class="event c-sage" style="left:277px;top:259px">
    <h3>Clinic<br>Expansion</h3>
    <p>Marrowfen moves offices twice in Kelsby due to growth &amp; expansion. Clinic established.</p>
  </div>

  <div class="badge-circle" style="left:647px;top:255px;border:2px solid var(--ink)"></div>
  <div class="event c-sage" style="left:689px;top:248px;width:180px">
    <h3>Fair-Enterprise</h3>
    <p>Marrowfen becomes a accredited Fair-Enterprise having met the highest standards of environmental social &amp; community performance</p>
  </div>

  <div class="icon c-peach" style="left:876px;top:83px"><svg viewBox="0 0 34 34" stroke="currentColor"><rect x="7" y="4" width="20" height="26" rx="2"/><path d="M11 11l2 2 3-3M19 12h5M11 19l2 2 3-3M19 20h5"/></svg></div>
  <div class="event c-peach" style="left:911px;top:83px;width:200px">
    <h3>Reconciliation<br>Action Plan (RAP)</h3>
    <p>Marrowfen’s Reflect RAP developed &amp; endorsed.</p>
  </div>
  <div class="icon c-peach" style="left:876px;top:165px"><svg viewBox="0 0 34 34" stroke="currentColor"><circle cx="17" cy="9" r="4"/><path d="M10 20a7 7 0 0 1 14 0"/><circle cx="9" cy="23" r="3"/><circle cx="25" cy="23" r="3"/><path d="M4 31a5 5 0 0 1 10 0M20 31a5 5 0 0 1 10 0"/></svg></div>
  <div class="event c-peach" style="left:911px;top:165px;width:200px">
    <h3>Client Advisory<br>Group</h3>
    <p>Marrowfen’s Client Advisory Group commences</p>
  </div>
  <div class="icon c-peach" style="left:876px;top:250px"><svg viewBox="0 0 34 34" stroke="currentColor"><rect x="4" y="6" width="26" height="18" rx="1"/><path d="M13 29h8M17 24v5M11 11h5M11 15h9"/></svg></div>
  <div class="event c-peach" style="left:911px;top:252px;width:200px">
    <h3>E-Learning Platform</h3>
    <p>Marrowfen e-learning platform launched</p>
  </div>
  <div class="badge-circle" style="left:879px;top:314px;background:var(--peach)"></div>
  <div class="event c-peach" style="left:915px;top:316px;width:196px">
    <h3>Spectrum Mark</h3>
    <p>Marrowfen achieves Spectrum Mark accreditation</p>
  </div>

  <div class="wordmark c-sage" style="left:40px;top:640px;font-size:11px">Marrowfen</div>
  <div class="event c-sage" style="left:114px;top:616px;width:160px">
    <h3>Marrowfen<br>Commences</h3>
    <p>Ingrid started the business with 25 years’ experience working for government &amp; non-government disability &amp; community services. Our first office is in Kelsby.</p>
  </div>
  <div class="badge-square" style="left:60px;top:784px"></div>
  <div class="event c-slate" style="left:114px;top:784px;width:150px">
    <h3>CareScheme Provider</h3>
    <p>Marrowfen becomes a CareScheme Registered Provider.</p>
  </div>

  <div class="icon c-peach" style="left:400px;top:620px"><svg viewBox="0 0 34 34" stroke="currentColor"><path d="M17 26s8-8 8-14a8 8 0 0 0-16 0c0 6 8 14 8 14z"/><circle cx="17" cy="12" r="3"/><path d="M6 30h22"/></svg></div>
  <div class="event c-peach" style="left:434px;top:616px;width:160px">
    <h3>Move to<br>Dunmere</h3>
    <p>Marrowfen moves to Dunmere due to further growth &amp; expansion.</p>
  </div>

  <div class="wordmark c-slate" style="left:708px;top:620px;font-size:12px">Vantell</div>
  <div class="event c-slate" style="left:760px;top:616px;width:200px">
    <h3>Vantell Best<br>of Business</h3>
    <p>Marrowfen wins the Vantell Best of Business Award (Vic) for building communities.</p>
  </div>
  <div class="icon c-slate" style="left:720px;top:706px"><svg viewBox="0 0 34 34" stroke="currentColor"><path d="M17 26s8-8 8-14a8 8 0 0 0-16 0c0 6 8 14 8 14z"/><circle cx="17" cy="12" r="3"/><path d="M6 30h22"/></svg></div>
  <div class="event c-slate" style="left:760px;top:711px;width:200px">
    <h3>Move to Ashvale</h3>
    <p>Marrowfen moves to a larger premises in Ashvale.</p>
  </div>
  <div class="icon c-slate" style="left:718px;top:770px"><svg viewBox="0 0 34 34" stroke="currentColor"><path d="M3 14l6-5 6 3 4-2 5 1 7 5"/><path d="M9 9l-6 8 9 8 3-2 3 3 3-2 3 2 5-6"/><path d="M15 12l-4 4 2 2 5-3"/></svg></div>
  <div class="event c-slate" style="left:760px;top:775px;width:210px">
    <h3>Partnerships</h3>
    <p>Partnerships established with Harbourview School for Children with Disability &amp; Wirrinda Centre (Southbank University)</p>
  </div>
</div>
</body>
</html>
```